Window company.

Hello,

We are a small family business located in Madrid, Spain that works nationwide to fix, change or mount the windows of your home / premises.

The group of possible clients to whom the flyer is focused ranges from 30 to 65 years, families in general who want comfort at home and extra savings every year in heating.

It must include not only graphics and a striking aesthetic in accordance with the concepts of wanting to reach / transmit the final product to the customer to sell the product.

Details to also include:

-Brief history of the company and its foundation in 2006. It will be subsequently translated into Spanish so put in words what you consider necessary so that the client stays with the concept that we are professionals.

--Specialized in exterior aluminum and PVC carpentry.

-We move to your home for a first visit and we provide the budget totally free without any commitment.

- Also payment facilities; up to 3 times, without interest.

-Contact details of the company. (WhatsApp, email, phone and location)
Open: Mon - Friday 11,00am - 9pm
Saturday: 12,00am - 7pm
Sunday: Closed

Also as a suggestion, to decide on your own, graphics of types of window openings, if you consider that anything that is striking for the client so it wonr be yet another advertising flyer.

We are open to all kinds of ideas, all of them involving marketing branding.

We are open to any type of idea and we want to stand out, the construction world is tough and we have an idea to grow, taking into account that it must not only be beautiful but commercial to attract potential customers with all kinds of purchasing power.

Thank you.

```html
<!DOCTYPE html>
<html lang="en">
<head>
<meta charset="utf-8">
<title>Vitrana – Window Flyer</title>
<link href="https://fonts.googleapis.com/css2?family=Roboto+Condensed:wght@400;700&family=Montserrat:wght@400;600;700&display=swap" rel="stylesheet">
<style>
  :root{
    --red:#e31a1a;
    --dark:#434343;
    --panel:#4b4b4b;
    --light:#efefef;
    --white:#ffffff;
    --ink:#2b2b2b;
    --logo-grey:#8a8a8a;
    --canvas:#e2e3e1;
  }
  *{margin:0;padding:0;box-sizing:border-box}
  html,body{width:1200px;height:2245px;overflow:hidden;background:var(--canvas)}
  .flyer{
    position:absolute;left:40px;top:331px;
    width:742px;height:1048px;
    transform:scale(1.5094);transform-origin:0 0;
    background:var(--white);overflow:hidden;
    font-family:"Montserrat",sans-serif;color:var(--ink);
  }
  .shapes{position:absolute;inset:0;width:742px;height:1048px}
  .abs{position:absolute}
  .condensed{font-family:"Roboto Condensed",sans-serif}

  .brand{left:40px;top:92px;display:flex;align-items:center;gap:14px}
  .brand-mark{width:22px;height:22px;background:var(--red)}
  .brand-name{font-family:"Roboto Condensed",sans-serif;font-size:46px;font-weight:700;color:var(--logo-grey);letter-spacing:1px;line-height:1}

  .headline{left:45px;top:270px;width:275px;text-align:center;color:var(--white);
    font-family:"Roboto Condensed",sans-serif;font-size:37px;line-height:45px;text-transform:uppercase}

  .about-title{left:45px;top:531px;color:var(--white);font-family:"Roboto Condensed",sans-serif;font-size:23px;line-height:28px}
  .about-text{left:45px;top:588px;width:650px;font-size:11.3px;line-height:15px;text-align:justify;color:#333}

  .provide-title{left:60px;top:740px;color:var(--white);font-family:"Roboto Condensed",sans-serif;font-size:22px}
  .service{left:60px;width:250px;display:flex;gap:12px;color:var(--white);font-size:11px;line-height:14.5px}
  .service .icon{flex:0 0 40px;width:40px;height:40px}
  .service p{text-align:justify;letter-spacing:.3px}
  .service b{font-weight:700}
  .service-visit{top:796px}
  .service-pay{top:880px}

  .call{left:45px;top:972px;color:var(--white)}
  .call-label{font-size:22px;font-weight:700;letter-spacing:.5px}
  .call-number{font-family:"Roboto Condensed",sans-serif;font-size:32px;margin-top:4px;letter-spacing:.5px}

  .hours-title{left:422px;top:756px;color:var(--red);font-family:"Roboto Condensed",sans-serif;font-size:23px;border-bottom:1.5px solid var(--red);line-height:26px}
  .hours{left:425px;top:778px;width:252px;border-collapse:separate;border-spacing:0 8px;font-size:11px;font-weight:700;margin-top:-8px}
  .hours td{border:1px solid var(--dark);height:19px;padding:0 5px;background:var(--white)}
  .hours td+td{border-left:none;text-align:center}
  .hours td:first-child{width:115px}

  .photo-small{top:867px;width:122px;height:98px;border:2px solid #9aa4a8}
  .photo-open{left:425px;background:linear-gradient(160deg,#3d7f86,#c9d3d6 55%,#9aa79a)}
  .photo-person{left:555px;background:linear-gradient(160deg,#f2f2f2,#b7bdc1 60%,#6d6f72)}

  .contact{left:460px;color:var(--white);display:flex;align-items:center;gap:10px}
  .contact svg{width:12px;height:12px}
  .contact-mail{top:1002px;font-size:13.5px}
  .contact-place{top:1025px;font-size:11px}
</style>
</head>
<body>
<main class="flyer">
  <svg class="shapes" viewBox="0 0 742 1048" aria-hidden="false">
    <defs>
      <linearGradient id="sofaScene" x1="0" y1="0" x2="1" y2="1">
        <stop offset="0" stop-color="#c8ccc9"/>
        <stop offset=".45" stop-color="#a9aca8"/>
        <stop offset=".75" stop-color="#b79a4a"/>
        <stop offset="1" stop-color="#7f8360"/>
      </linearGradient>
      <linearGradient id="lowerBg" x1="0" y1="0" x2="1" y2="0">
        <stop offset="0" stop-color="#ffffff"/>
        <stop offset="1" stop-color="#eeeeee"/>
      </linearGradient>
    </defs>
    <polygon points="0,208 345,208 543,18 742,205 742,525 0,525" fill="url(#sofaScene)" role="img" aria-label="Photo: two smiling women relaxing on a grey sofa in front of large aluminium windows"/>
    <polyline points="345,206 543,16 742,203" fill="none" stroke="var(--red)" stroke-width="4"/>
    <rect x="45" y="208" width="275" height="317" fill="var(--panel)" opacity=".94"/>
    <rect x="0" y="525" width="742" height="187" fill="var(--light)"/>
    <rect x="0" y="523" width="742" height="4" fill="var(--red)"/>
    <polygon points="0,525 190,525 165,566 0,566" fill="var(--red)"/>
    <rect x="0" y="712" width="742" height="336" fill="url(#lowerBg)"/>
    <rect x="45" y="713" width="293" height="237" fill="var(--red)"/>
    <polygon points="0,950 370,950 443,1048 0,1048" fill="var(--dark)"/>
    <polygon points="408,992 742,992 742,1048 451,1048" fill="var(--red)"/>
  </svg>

  <div class="abs brand"><span class="brand-mark"></span><span class="brand-name">VITRANA</span></div>

  <h1 class="abs headline">We specialized in exterior aluminum and PVC carpentry</h1>

  <h2 class="abs about-title">ABOUT US</h2>
  <p class="abs about-text">Lorem Ipsum is simply dummy text of the printing and typesetting industry. Lorem Ipsum has been the industry's standard dummy text ever since the 1500s, when an unknown printer took a galley of type and scrambled it to make a type specimen book. It has survived not only five centuries, but also the leap into electronic typesetting, remaining essentially unchanged. It was popularised in the 1960s with the release of Letraset sheets containing Lorem Ipsum passages, and more recently with desktop publishing software like Aldus PageMaker including versions of Lorem Ipsum.</p>

  <h2 class="abs provide-title">WE PROVIDE</h2>
  <div class="abs service service-visit">
    <svg class="icon" viewBox="0 0 40 40" fill="none" stroke="#fff" stroke-width="1.4">
      <rect x="1" y="1" width="38" height="38" rx="7"/>
      <path d="M8 20l6-5 5 2 4-3 9 6M12 22l5 4 3-2 3 3 3-2 4-3M17 26l2 2"/>
    </svg>
    <p>We move to your home for a first visit and we provide the <b>budget totally free without any commitment.</b></p>
  </div>
  <div class="abs service service-pay">
    <svg class="icon" viewBox="0 0 40 40" fill="none" stroke="#fff" stroke-width="1.4">
      <rect x="1" y="1" width="38" height="38" rx="7"/>
      <rect x="8" y="12" width="20" height="13" rx="1.5"/>
      <rect x="12" y="16" width="20" height="13" rx="1.5"/>
      <path d="M12 20h20M15 25h6"/>
    </svg>
    <p><b>Payment facilities</b><br>up to 3 times, without interest.</p>
  </div>

  <div class="abs call">
    <div class="call-label">Call or WhatsApp now</div>
    <div class="call-number">910-4827-3316</div>
  </div>

  <h2 class="abs hours-title">OPENING HOURS</h2>
  <table class="abs hours">
    <tr><td>Mon - Friday</td><td>11:00am - 9pm</td></tr>
    <tr><td>Saturday</td><td>12:00am - 7pm</td></tr>
    <tr><td>Sunday</td><td>Closed</td></tr>
  </table>

  <div class="abs photo-small photo-open" role="img" aria-label="Photo: open casement window in a teal wall"></div>
  <div class="abs photo-small photo-person" role="img" aria-label="Photo: woman opening a white PVC window"></div>

  <div class="abs contact contact-mail">
    <svg viewBox="0 0 12 12" fill="none" stroke="#fff" stroke-width="1"><circle cx="6" cy="6" r="5"/><path d="M1 6h10M6 1c-3 3-3 7 0 10M6 1c3 3 3 7 0 10"/></svg>
    <span>hola@vitrana-ventanas.es</span>
  </div>
  <div class="abs contact contact-place">
    <svg viewBox="0 0 12 12" fill="#fff"><path d="M6 0a4 4 0 0 0-4 4c0 3 4 8 4 8s4-5 4-8a4 4 0 0 0-4-4zm0 5.5a1.5 1.5 0 1 1 0-3 1.5 1.5 0 0 1 0 3z"/></svg>
    <span>Lorem Ipsum, is simply dummy text</span>
  </div>
</main>
</body>
</html>
```